Sex Trafficked women Empowered Business Card Design Project

I would like a two-sided business card. On the front, please include: Marta Oberlin, Executive Director 555-284-7316, www.tallowcrest.org, marta@tallowcrest.org and logo.

On the back:
Vision
Survivors of sexual exploitation live free, fulfilling their God-given purpose.

Perhaps a QR code to direct them to the website: www.tallowcrest.org

I want to try a deeper color for the logo. i have added these files.

My desire is to communicate hope, freedom and new life.
Updates

i decided to ask for business card designs with a deeper toned logo. see new files attached

i have placed the vertical logo as an option, but i would still want the logo with tagline used.

Target Market(s)

I want a professional look to appeal to donors who have a heart to help sexually exploited women. I chose a logo that was light enough to look good on a variety of backgrounds. I do want the logo to catch attention.

Industry/Entity Type

Business

Font styles to use
Serif

Requirements
Must have
• i want to be able to read the tagline. Also, the design should match the look and feel of the logo.

Nice to have
• Since there isn't much text on the back, feel free to be a bit more creative. I still want a professional look.

```html
<!DOCTYPE html>
<html lang="en">
<head>
<meta charset="utf-8">
<title>Tallowcrest Business Card</title>
<link rel="stylesheet" href="https://fonts.googleapis.com/css2?family=Cinzel:wght@600&family=Libre+Baskerville:ital,wght@0,700;1,400&family=Lato:wght@700;900&display=swap">
<style>
  :root {
    --backdrop: #2b2b2d;
    --card-top: #ffffff;
    --card-bottom: #e4e5e7;
    --brand-blue: #1e88e5;
    --ink: #1c1c1c;
    --ink-soft: #3a3a3a;
    --white: #ffffff;
  }
  * { margin: 0; padding: 0; box-sizing: border-box; }
  html, body {
    width: 1200px; height: 985px; overflow: hidden;
    background: var(--backdrop);
  }
  .stage { position: relative; width: 1200px; height: 985px; }

  .card {
    position: absolute;
    width: 560px; height: 320px;
    border-radius: 20px;
    background: linear-gradient(160deg, var(--card-top) 0%, var(--card-bottom) 100%);
    box-shadow: 0 18px 40px rgba(0,0,0,.55);
    overflow: hidden;
  }
  .card::before {
    content: ""; position: absolute; inset: 9px;
    border: 3px solid var(--brand-blue); border-radius: 14px;
    pointer-events: none;
  }
  .card--back { left: 90px; top: 110px; }
  .card--front { left: 550px; top: 530px; }

  .brand {
    position: absolute; display: flex; align-items: center; gap: 16px;
  }
  .brand__mark {
    width: 62px; height: 62px; border-radius: 50%;
    background: var(--brand-blue); flex: none;
  }
  .brand__name {
    font-family: "Cinzel", serif; font-weight: 600;
    font-size: 38px; letter-spacing: 1px; color: var(--ink); line-height: 1;
  }
  .brand__tagline {
    font-family: "Libre Baskerville", serif; font-style: italic;
    font-size: 14px; color: var(--ink-soft); margin-top: 6px; text-align: right;
  }

  .card--back .brand { left: 70px; top: 70px; }
  .vision {
    position: absolute; left: 70px; right: 60px; top: 185px;
    font-family: "Libre Baskerville", serif; font-weight: 700;
    font-size: 19px; line-height: 1.55; color: var(--ink-soft); text-align: center;
  }

  .card--front .brand { left: 110px; top: 56px; }
  .holder { position: absolute; left: 12px; top: 212px; }
  .holder__name {
    display: inline-block; margin-left: 72px;
    background: var(--brand-blue); color: var(--white);
    font-family: "Lato", sans-serif; font-weight: 900; font-size: 22px;
    padding: 4px 14px; border-radius: 6px 6px 0 0;
  }
  .holder__bar { width: 300px; height: 12px; background: var(--brand-blue); }
  .holder__title {
    margin-left: 84px; margin-top: 4px;
    font-family: "Lato", sans-serif; font-weight: 700; font-size: 20px; color: var(--ink-soft);
  }

  .contacts { position: absolute; right: 40px; top: 168px; list-style: none; }
  .contacts li {
    display: flex; align-items: center; gap: 10px; margin-bottom: 12px;
    font-family: "Lato", sans-serif; font-weight: 700; font-size: 18px; color: var(--ink);
  }
  .contacts svg { width: 26px; height: 26px; flex: none; }

  .website {
    position: absolute; right: 12px; bottom: 12px;
    background: var(--brand-blue); color: var(--white);
    font-family: "Lato", sans-serif; font-weight: 700; font-size: 16px;
    padding: 6px 16px 6px 18px; border-radius: 10px 0 11px 0;
  }
</style>
</head>
<body>
<main class="stage">

  <section class="card card--back" aria-label="Card back">
    <div class="brand">
      <span class="brand__mark"></span>
      <div>
        <div class="brand__name">Tallowcrest</div>
        <div class="brand__tagline">Where new light rises</div>
      </div>
    </div>
    <p class="vision">Survivors of sexual exploitation live free,<br>fulfilling their God-given purpose.</p>
  </section>

  <section class="card card--front" aria-label="Card front">
    <div class="brand">
      <span class="brand__mark"></span>
      <div>
        <div class="brand__name">Tallowcrest</div>
        <div class="brand__tagline">Where new light rises</div>
      </div>
    </div>

    <div class="holder">
      <span class="holder__name">DORIAN PELL</span>
      <div class="holder__bar"></div>
      <div class="holder__title">Managing Director</div>
    </div>

    <ul class="contacts">
      <li>
        <svg viewBox="0 0 26 26" aria-hidden="true">
          <rect width="26" height="26" rx="4" fill="var(--brand-blue)"/>
          <path d="M8 7c1-1 2-1 3 0l1.5 2c.5.8.3 1.5-.3 2l-.8.6c.6 1.6 1.7 2.8 3.2 3.5l.7-.8c.5-.6 1.3-.7 2-.2l2 1.4c.9.7.9 1.8 0 2.7-1.4 1.4-3.3 1.4-5.8-.1-2.3-1.4-4.2-3.4-5.4-5.8C6.8 10.2 6.8 8.3 8 7z" fill="var(--white)"/>
        </svg>
        555-284-7316
      </li>
      <li>
        <svg viewBox="0 0 26 26" aria-hidden="true">
          <rect width="26" height="26" rx="4" fill="var(--brand-blue)"/>
          <rect x="5" y="8" width="16" height="11" rx="1" fill="var(--white)"/>
          <path d="M5.5 8.5 13 14l7.5-5.5" fill="none" stroke="var(--brand-blue)" stroke-width="1.6"/>
        </svg>
        marta@tallowcrest.org
      </li>
    </ul>

    <div class="website">www.tallowcrest.org</div>
  </section>

</main>
</body>
</html>
```